Dental office needs a newspaper ad to encourage new patients to join our practice

"October Teeth Whitening Special" Call today to schedule your next dental cleaning and exam and receive a free bleach kit. (small disclaimer at the bottom of the ad) Dr. Halvorsen and his staff follow the most up-to-date NHA infection control guidelines to protect our patients from CoVid-19 exposure. We offer a full spectrum of dental services including oral surgery, implants, root canals and cosmetic crowns and bridges. Our staff of licensed dental hygienists provide continued periodontal care for the healthiest teeth and gums. Visit our website. These are just some ideas you might be able to use. Also mention that most insurances are accepted. Emergencies and new patients welcome. As softer southern style motif like in our website can be used as a backdrop. The color scheme of the business logo and stationery is the same as the website.
Target Market(s)
All ages, local population 8,000 southern farming community. White Hispanic older population. Not oriented towards children.
Requirements
Must have
- Nice color. See our website at halvorsendentalcare.example for basic image of practice
Nice to have
- It will be a quarter to half page in a local newspaper, so it can be good sized with plenty of print an graphics

```html
<!DOCTYPE html>
<html lang="en">
<head>
<meta charset="utf-8">
<title>Halvorsen Dental – October Newspaper Ad</title>
<link href="https://fonts.googleapis.com/css2?family=Montserrat:wght@300;400&family=Open+Sans:wght@400;600;700&family=Oswald:wght@400;600&display=swap" rel="stylesheet">
<style>
  :root{
    --stage:#5c5c5c;
    --stage-light:#8a8a8a;
    --blue:#1466b8;
    --blue-deep:#0e55a6;
    --blue-light:#22a6ee;
    --green:#2cb24b;
    --green-bright:#35d16a;
    --white:#ffffff;
    --photo-top:#4d5a52;
    --photo-bottom:#1f3d55;
  }
  *{margin:0;padding:0;box-sizing:border-box}
  html,body{width:1200px;height:600px;overflow:hidden}
  body{
    background:linear-gradient(160deg,var(--stage-light),var(--stage));
    position:relative;
    font-family:"Open Sans",Arial,sans-serif;
  }
  .ad{
    position:absolute;left:384px;top:20px;width:432px;height:560px;
    background:var(--blue);overflow:hidden;color:var(--white);
  }
  .ad__photo{
    position:absolute;left:0;top:0;width:432px;height:290px;
    background:linear-gradient(180deg,var(--photo-top) 0%,#2f4a4c 45%,var(--photo-bottom) 100%);
  }
  .ad__waves{position:absolute;left:0;top:0}
  .brand{
    position:absolute;left:93px;top:26px;height:64px;width:250px;
    display:flex;align-items:center;
  }
  .brand__pill{
    position:absolute;left:28px;top:13px;width:222px;height:34px;
    background:var(--white);border:3px solid var(--blue);border-radius:18px;
  }
  .brand__dot{
    position:relative;width:64px;height:64px;border-radius:50%;
    background:var(--white);border:3px solid var(--blue);flex:none;
  }
  .brand__name{
    position:relative;margin-left:-2px;
    font-weight:700;font-size:15.5px;color:var(--blue);white-space:nowrap;
  }
  .headline{
    position:absolute;left:0;width:100%;top:110px;text-align:center;
    font-family:"Montserrat",Arial,sans-serif;font-weight:300;
    font-size:22px;line-height:29px;
  }
  .headline__top{letter-spacing:9px;margin-left:9px}
  .headline__bottom{letter-spacing:0.5px}
  .special{
    position:absolute;left:97px;top:174px;width:106px;height:106px;border-radius:50%;
    background:var(--blue);border:3px solid var(--blue-light);
    display:flex;align-items:center;justify-content:center;text-align:center;
    font-weight:700;font-size:13px;line-height:17px;letter-spacing:.3px;
  }
  .services{
    position:absolute;left:0;width:100%;top:286px;text-align:center;
    font-weight:700;font-size:12.6px;line-height:17.5px;
  }
  .rule{position:absolute;left:38px;width:356px;top:341px;height:1px;background:var(--white)}
  .hygiene{
    position:absolute;left:0;width:100%;top:349px;text-align:center;
    font-size:11.6px;line-height:16px;
  }
  .insurance{
    position:absolute;left:85px;top:384px;width:262px;height:24px;
    background:var(--green-bright);
    clip-path:polygon(0 0,100% 0,96% 50%,100% 100%,0 100%,4% 50%);
    display:flex;align-items:center;justify-content:center;
    font-family:"Oswald",Arial,sans-serif;font-size:17px;
  }
  .cta-frame{
    position:absolute;left:27px;top:424px;width:380px;height:66px;
    border:1px solid var(--white);
  }
  .cta-title{
    position:absolute;left:0;width:100%;top:412px;text-align:center;
    font-family:"Oswald",Arial,sans-serif;font-weight:600;font-size:26px;line-height:34px;
  }
  .cta-title span,.phone span{background:var(--blue);padding:0 12px}
  .cta-offer{
    position:absolute;left:46px;top:448px;width:344px;height:24px;background:var(--white);
    display:flex;align-items:center;justify-content:center;
    font-family:"Oswald",Arial,sans-serif;font-size:12.6px;color:var(--green);
  }
  .phone{
    position:absolute;left:0;width:100%;top:474px;text-align:center;
    font-weight:700;font-size:30px;line-height:36px;letter-spacing:.5px;
  }
  .phone svg{vertical-align:-3px;margin-right:6px}
  .contact{
    position:absolute;left:0;top:512px;width:100%;height:23px;background:var(--green);
    display:flex;align-items:center;justify-content:center;gap:10px;font-size:11px;
  }
  .contact__sep{width:1px;height:13px;background:var(--white)}
  .contact svg{vertical-align:-2px;margin-right:4px}
  .disclaimer{
    position:absolute;left:0;width:100%;top:541px;text-align:center;font-size:5.4px;
  }
</style>
</head>
<body>
  <article class="ad">
    <div class="ad__photo" role="img" aria-label="Photo of the dental team standing in front of the practice building among trees"></div>

    <svg class="ad__waves" width="432" height="560" viewBox="0 0 432 560" aria-hidden="true">
      <defs>
        <linearGradient id="lightBand" x1="0" x2="1">
          <stop offset="0" stop-color="#22a6ee"/><stop offset="1" stop-color="#1a7fd6"/>
        </linearGradient>
      </defs>
      <path d="M0 207 C90 190 170 205 230 240 C300 280 380 250 432 205 L432 560 L0 560Z" fill="url(#lightBand)"/>
      <path d="M0 250 C70 215 150 220 210 258 C280 300 370 290 432 245 L432 560 L0 560Z" fill="var(--green-bright)"/>
      <path d="M0 272 C70 240 150 240 210 266 C280 298 370 292 432 250 L432 560 L0 560Z" fill="var(--white)"/>
      <path d="M0 285 C70 255 150 252 210 275 C280 302 370 300 432 258 L432 560 L0 560Z" fill="var(--blue)"/>
    </svg>

    <div class="brand">
      <div class="brand__pill"></div>
      <div class="brand__dot"></div>
      <div class="brand__name">Erik J. Halvorsen, DMD</div>
    </div>

    <h1 class="headline">
      <div class="headline__top">EMERGENCIES AND</div>
      <div class="headline__bottom">NEW PATIENTS WELCOME.</div>
    </h1>

    <div class="special">OCTOBER<br>TEETH<br>WHITENING<br>SPECIAL</div>

    <p class="services">We Offer A Full Spectrum Of Dental Services<br>Including Oral Surgery, Implants, Root Canals and<br>Cosmetic Crowns And Bridges.</p>
    <div class="rule"></div>
    <p class="hygiene">Our staff of licensed dental hygienists provide continued periodontal<br>care for the healthiest teeth and gums.</p>

    <div class="insurance">MOST INSURANCES ARE ACCEPTED</div>

    <div class="cta-frame"></div>
    <h2 class="cta-title"><span>CALL TODAY TO SCHEDULE</span></h2>
    <div class="cta-offer">your next dental cleaning and exam and receive a free bleach kit.</div>
    <div class="phone"><span><svg width="26" height="26" viewBox="0 0 26 26" aria-hidden="true"><circle cx="13" cy="13" r="11.5" fill="none" stroke="#fff" stroke-width="2"/><path d="M9 7.5c1-.6 1.6-.4 2.1.6l.8 1.7c.3.7.1 1.2-.5 1.6l-.7.5c.5 1.5 1.5 2.8 2.9 3.7l.6-.6c.5-.5 1-.6 1.6-.2l1.6 1c.8.5.9 1.2.3 2-.8 1.1-2 1.5-3.3 1-3.4-1.3-6-4.4-6.6-8-.2-1.3.2-2.5 1.2-3.3z" fill="#fff"/></svg>555-014-2278</span></div>

    <div class="contact">
      <span><svg width="9" height="12" viewBox="0 0 9 12" aria-hidden="true"><circle cx="4.5" cy="4" r="3" fill="none" stroke="#fff" stroke-width="1.3"/><path d="M4.5 7v4M1 11.3h7" stroke="#fff" stroke-width="1.3"/></svg>18 Magnolia St Fairhaven, FL 33900</span>
      <span class="contact__sep"></span>
      <span><svg width="13" height="9" viewBox="0 0 13 9" aria-hidden="true"><rect x=".6" y=".6" width="11.8" height="7.8" fill="none" stroke="#fff" stroke-width="1.1"/><path d="M.6.6l5.9 4.6L12.4.6" fill="none" stroke="#fff" stroke-width="1.1"/></svg>fairhavensmiles@example.com</span>
    </div>

    <p class="disclaimer">Disclaimer* Dr. Halvorsen and his staff follow the most up-to-date NHA infection control guidelines to protect our patients from CoVid-19 exposure.</p>
  </article>
</body>
</html>
```